PELDRAX Business Cards

We require a business card for our company that provides IT consulting services. We already have a logo that needs to be used on the card. We want a clean professional looking design that incorporates our colours. Our main focus is providing managed services to business, which involves us looking after all of their IT requirements including managing servers/networks, projects, and procurement.

Industry/Entity Type

Information Technology

Requirements
Must have
• our logo, contact information, name, title, phone numbers

```html
<!DOCTYPE html>
<html lang="en">
<head>
<meta charset="utf-8">
<title>PELDRAX Business Cards</title>
<link href="https://fonts.googleapis.com/css2?family=Poppins:wght@400;500;600&display=swap" rel="stylesheet">
<style>
  :root {
    --stage: #2b2d30;
    --card-black: #141516;
    --brand-blue: #1a9ad6;
    --paper-white: #ffffff;
    --text-light: #e6e6e6;
  }
  * { margin: 0; padding: 0; box-sizing: border-box; }
  html, body { width: 1200px; height: 900px; overflow: hidden; }
  body {
    background: var(--stage);
    font-family: "Poppins", sans-serif;
    position: relative;
  }
  .card {
    position: absolute;
    width: 560px;
    height: 320px;
    left: 320px;
    background: var(--card-black);
    overflow: hidden;
    box-shadow: 0 14px 30px rgba(0,0,0,0.45);
  }
  .card-shapes { position: absolute; inset: 0; }

  /* Brand face */
  .card--brand { top: 80px; }
  .brand-mark {
    position: absolute;
    left: 0; right: 0; top: 118px;
    display: flex; align-items: center; justify-content: center; gap: 18px;
  }
  .brand-dot {
    width: 34px; height: 34px; border-radius: 50%;
    background: var(--brand-blue);
  }
  .brand-name {
    color: var(--brand-blue);
    font-weight: 600;
    font-size: 58px;
    letter-spacing: 4px;
    line-height: 1;
  }

  /* Contact face */
  .card--contact { top: 480px; }
  .contact-block {
    position: absolute; left: 34px; top: 30px;
    color: var(--text-light);
  }
  .person-name {
    color: var(--brand-blue);
    font-weight: 500;
    font-size: 22px;
    letter-spacing: 0.5px;
  }
  .person-title { font-size: 15px; margin-top: -2px; }
  .divider {
    width: 18px; height: 2px; background: var(--brand-blue);
    margin: 14px 0 12px;
  }
  .address { font-size: 12px; line-height: 1.5; margin-bottom: 10px; }
  .contact-line {
    display: flex; align-items: center; gap: 10px;
    font-size: 12px; margin-top: 6px;
  }
  .contact-line svg { width: 14px; height: 14px; fill: var(--brand-blue); }
  .web-tab {
    position: absolute; left: 0; top: 258px;
    width: 200px; height: 30px;
    background: var(--paper-white);
    border-radius: 0 14px 0 0;
    padding-left: 26px;
    display: flex; align-items: center;
    color: var(--brand-blue);
    font-size: 14px; font-weight: 500;
  }
  .contact-mark {
    position: absolute; left: 350px; top: 228px;
    display: flex; align-items: center; gap: 10px;
  }
  .contact-mark .brand-dot { width: 20px; height: 20px; }
  .contact-mark .brand-name { font-size: 30px; letter-spacing: 2px; }
</style>
</head>
<body>

  <section class="card card--brand">
    <svg class="card-shapes" viewBox="0 0 560 320" aria-hidden="true">
      <rect x="0" y="282" width="560" height="5" fill="var(--paper-white)"/>
      <rect x="0" y="290" width="560" height="30" fill="var(--brand-blue)"/>
    </svg>
    <div class="brand-mark">
      <span class="brand-dot"></span>
      <span class="brand-name">PELDRAX</span>
    </div>
  </section>

  <section class="card card--contact">
    <svg class="card-shapes" viewBox="0 0 560 320" aria-hidden="true">
      <path d="M240,320 C250,250 320,205 420,205 C490,205 505,140 560,130 L560,320 Z" fill="var(--paper-white)"/>
      <rect x="0" y="288" width="560" height="32" fill="var(--paper-white)"/>
      <rect x="0" y="296" width="560" height="4" fill="var(--brand-blue)"/>
      <rect x="0" y="306" width="260" height="14" fill="var(--brand-blue)"/>
    </svg>

    <div class="contact-block">
      <div class="person-name">MARLOW KESSING</div>
      <div class="person-title">owner</div>
      <div class="divider"></div>
      <div class="address">48 Alder Road<br>Box 902, Fenwick, AB</div>
      <div class="contact-line">
        <svg viewBox="0 0 24 24" aria-hidden="true"><path d="M6.6 10.8a15.1 15.1 0 0 0 6.6 6.6l2.2-2.2a1 1 0 0 1 1-.25 11.4 11.4 0 0 0 3.6.57 1 1 0 0 1 1 1V20a1 1 0 0 1-1 1A17 17 0 0 1 3 4a1 1 0 0 1 1-1h3.5a1 1 0 0 1 1 1c0 1.25.2 2.45.57 3.57a1 1 0 0 1-.25 1z"/></svg>
        <span>403-555-0182</span>
      </div>
      <div class="contact-line">
        <svg viewBox="0 0 24 24" aria-hidden="true"><path d="M2 5h20v14H2z M2 5l10 8 10-8" fill="var(--brand-blue)" stroke="var(--card-black)" stroke-width="1.5"/></svg>
        <span>email@peldrax.com</span>
      </div>
    </div>

    <div class="web-tab">www.peldrax.com</div>

    <div class="contact-mark">
      <span class="brand-dot"></span>
      <span class="brand-name">PELDRAX</span>
    </div>
  </section>

</body>
</html>
```